依頼概要
■依頼の目的/概要
当方販促で使用するメモ帳を販売しております。
今回は年末年始に企業様が挨拶に出向く時に使用するノベルティメモ帳の表紙及び本文のデザインをお願いします。

■依頼詳細
年末年始にお配りする販促用メモ帳の表紙のデザインをお願いします。表紙おもては縁起のいいデザイン、裏面はカレンダー、組み立てるとカレンダーとして使われるデザインを希望します。カレンダー部分はダミーでかまいません。採用決定しましたら細かい日付けなど修正お願いします。
使われる企業様は全国の企業様さまざまです。過去3年の実績デザインを添付しております。昨年も多数の提案がありました。採用に迷ったデザインも多数ありました。内容が変わらない提案でも歓迎します。

■重視するポイント
色使いなど制限はありませんが、縁起の良いデザインを希望いたします。テンプレートを添付しておりますのでご利用下さい。

その他何かご不明な点がございましたら、お気軽にご質問下さい。
よろしくお願いいたします。
■ 選んだ理由

社内でアンケートを取り、評価の良かったものを採用させていただきました。
年末年始の商品に相応しい、おめでたくどの年代の方にも好まれるデザインが決め手となりました。

■ 提案者全員のお礼・コメント

この度はたくさんのご提案ありがとうございました。
素敵な作品ばかりでその中で1点を選ぶのには大変苦労しました。
また次の機会にも是非ご提案頂ければと思っております。
ありがとうございました。

```html
<!DOCTYPE html>
<html lang="ja">
<head>
<meta charset="utf-8">
<title>2021年カレンダー提案</title>
<link rel="stylesheet" href="https://fonts.googleapis.com/css2?family=Noto+Serif+JP:wght@400;600;700&display=swap">
<style>
:root{
  --paper:#ffffff;
  --ink:#3a3a3a;
  --trim:#b9b9b9;
  --cream:#fff7b8;
  --cream-deep:#f7e46e;
  --gold:#e8c84a;
  --red:#c8313a;
  --navy:#2c3e86;
  --teal:#2a9a96;
  --green:#3d9a3a;
  --cal-line:#d8d8d8;
  --cal-text:#555;
}
*{box-sizing:border-box;margin:0;padding:0}
html,body{width:849px;height:1200px;overflow:hidden;background:var(--paper)}
body{position:relative;font-family:"Noto Serif JP",serif;color:var(--ink)}

.sheet-title{position:absolute;left:50px;top:64px;width:330px;height:54px;border:1.5px solid var(--ink);
  display:flex;align-items:center;padding-left:20px;font-size:20px;letter-spacing:1px}
.sheet-ornament{position:absolute;left:420px;top:20px;width:420px;height:110px;
  background:radial-gradient(circle at 85% 35%,#e7d7a8 0 10%,transparent 30%),linear-gradient(90deg,transparent,#f2ecdf 40%,#efe6d2);
  border-radius:6px;opacity:.8}

/* trim marks */
.trim{position:absolute;border-color:var(--trim);border-style:solid;border-width:0}
.trim.h{height:0;border-top-width:1px}
.trim.v{width:0;border-left-width:1px}

/* panels */
.panel{position:absolute;overflow:hidden}
.front{left:174px;top:140px;width:284px;height:880px;
  background:linear-gradient(180deg,var(--cream) 0%,#fff3a0 45%,var(--cream) 100%)}
.back-top{left:474px;top:140px;width:274px;height:440px;
  background:linear-gradient(180deg,var(--cream),#fff1a0)}
.back-bottom{left:474px;top:580px;width:274px;height:440px;background:var(--paper);
  border:1px solid var(--trim);border-top:none}
.fold-notch{position:absolute;left:0;top:0;width:274px;height:150px}

.artwork{position:absolute;border-radius:50%}
.band{position:absolute;border-radius:4px}

.calendar{position:absolute;background:var(--paper);padding:10px 10px 8px}
.calendar-title{font-size:10px;text-align:center;color:var(--cal-text);margin-bottom:6px;letter-spacing:.5px}
.months{display:grid;gap:6px 8px}
.month{font-size:4.6px;line-height:6.4px;color:var(--cal-text);border-top:1px solid var(--cal-line);padding-top:2px}
.month b{display:block;font-size:8px;line-height:10px;color:var(--red);font-weight:600}
.month p{word-spacing:1.4px}

.front .calendar{left:50px;top:110px;width:220px;height:310px;transform:rotate(180deg)}
.front .months{grid-template-columns:repeat(2,1fr)}
.back-top .calendar{left:10px;top:90px;width:254px;height:330px}
.back-top .months{grid-template-columns:repeat(3,1fr)}

.memo-title{position:absolute;left:14px;top:640px;color:var(--green);font-weight:700;line-height:1.05}
.memo-title .year{font-size:20px;display:block}
.memo-title .label{font-size:17px;display:block}

.brand{position:absolute;left:700px;top:1070px;display:flex;align-items:center;gap:8px;color:var(--teal);font-size:30px;letter-spacing:3px}
.brand .dot{width:18px;height:18px;border-radius:50%;background:var(--teal)}
.footer-band{position:absolute;left:0;bottom:0;width:849px;height:52px;background:var(--teal);
  color:#fff;font-size:15px;display:flex;align-items:center;justify-content:flex-end;padding-right:40px;letter-spacing:1px}
</style>
</head>
<body>

<div class="sheet-title">2021年カレンダー提案</div>
<div class="sheet-ornament" role="img" aria-label="金色の唐草模様と吊るされた雪の結晶の飾り"></div>

<!-- trim / fold guides -->
<div class="trim h" style="left:150px;top:140px;width:620px"></div>
<div class="trim h" style="left:150px;top:580px;width:620px"></div>
<div class="trim h" style="left:150px;top:1020px;width:620px"></div>
<div class="trim v" style="left:174px;top:118px;height:924px"></div>
<div class="trim v" style="left:458px;top:118px;height:924px"></div>
<div class="trim v" style="left:474px;top:118px;height:924px"></div>
<div class="trim v" style="left:748px;top:118px;height:924px"></div>

<!-- front cover -->
<section class="panel front" aria-label="表紙">
  <div class="band" style="left:0;top:0;width:284px;height:40px;background:linear-gradient(90deg,var(--cream-deep),var(--gold))" role="img" aria-label="金色の霞模様"></div>
  <div class="artwork" style="left:-30px;top:20px;width:120px;height:120px;background:radial-gradient(circle,#f29b9b,var(--navy))" role="img" aria-label="手毬と梅の花のイラスト"></div>
  <div class="artwork" style="left:200px;top:30px;width:110px;height:110px;background:radial-gradient(circle,#6fc7c0,#6a3fa0)" role="img" aria-label="手毬のイラスト"></div>
  <div class="artwork" style="left:210px;top:330px;width:100px;height:100px;background:radial-gradient(circle,#f7c8d0,var(--red))" role="img" aria-label="手毬と紐のイラスト"></div>

  <div class="calendar">
    <div class="calendar-title">2021 Calendar</div>
    <div class="months">
      <div class="month"><b>1</b><p>1 2 3 4 5 6 7<br>8 9 10 11 12 13 14<br>15 16 17 18 19 20 21<br>22 23 24 25 26 27 28<br>29 30 31</p></div>
      <div class="month"><b>2</b><p>1 2 3 4 5 6 7<br>8 9 10 11 12 13 14<br>15 16 17 18 19 20 21<br>22 23 24 25 26 27 28<br>29 30 31</p></div>
      <div class="month"><b>3</b><p>1 2 3 4 5 6 7<br>8 9 10 11 12 13 14<br>15 16 17 18 19 20 21<br>22 23 24 25 26 27 28<br>29 30 31</p></div>
      <div class="month"><b>4</b><p>1 2 3 4 5 6 7<br>8 9 10 11 12 13 14<br>15 16 17 18 19 20 21<br>22 23 24 25 26 27 28<br>29 30 31</p></div>
      <div class="month"><b>5</b><p>1 2 3 4 5 6 7<br>8 9 10 11 12 13 14<br>15 16 17 18 19 20 21<br>22 23 24 25 26 27 28<br>29 30 31</p></div>
      <div class="month"><b>6</b><p>1 2 3 4 5 6 7<br>8 9 10 11 12 13 14<br>15 16 17 18 19 20 21<br>22 23 24 25 26 27 28<br>29 30 31</p></div>
    </div>
  </div>

  <div class="band" style="left:0;top:470px;width:284px;height:30px;background:linear-gradient(90deg,var(--gold),var(--cream-deep))" role="img" aria-label="金色の霞模様"></div>
  <div class="artwork" style="left:120px;top:500px;width:150px;height:150px;background:radial-gradient(circle,#8fd3c9,var(--navy))" role="img" aria-label="手毬と紐のイラスト"></div>
  <div class="artwork" style="left:-20px;top:520px;width:100px;height:100px;background:radial-gradient(circle,#f7c8d0,#7a3fa0)" role="img" aria-label="手毬のイラスト"></div>

  <h1 class="memo-title"><span class="year">2021</span><span class="label">Calendar Memo</span></h1>

  <div class="artwork" style="left:-10px;top:700px;width:140px;height:140px;background:radial-gradient(circle,#79c7e0,#2c6a9a)" role="img" aria-label="手毬と梅の花のイラスト"></div>
  <div class="artwork" style="left:150px;top:740px;width:160px;height:160px;background:radial-gradient(circle,#f4a7a7,var(--red))" role="img" aria-label="手毬と紐のイラスト"></div>
</section>

<!-- back: calendar -->
<section class="panel back-top" aria-label="裏面カレンダー">
  <div class="band" style="left:0;top:0;width:274px;height:70px;background:linear-gradient(180deg,var(--cream-deep),var(--cream))" role="img" aria-label="金色の霞模様"></div>
  <div class="calendar">
    <div class="calendar-title">2021 Calendar</div>
    <div class="months">
      <div class="month"><b>1</b><p>1 2 3 4 5 6 7<br>8 9 10 11 12 13 14<br>15 16 17 18 19 20 21<br>22 23 24 25 26 27 28<br>29 30 31</p></div>
      <div class="month"><b>2</b><p>1 2 3 4 5 6 7<br>8 9 10 11 12 13 14<br>15 16 17 18 19 20 21<br>22 23 24 25 26 27 28<br>29 30 31</p></div>
      <div class="month"><b>3</b><p>1 2 3 4 5 6 7<br>8 9 10 11 12 13 14<br>15 16 17 18 19 20 21<br>22 23 24 25 26 27 28<br>29 30 31</p></div>
      <div class="month"><b>4</b><p>1 2 3 4 5 6 7<br>8 9 10 11 12 13 14<br>15 16 17 18 19 20 21<br>22 23 24 25 26 27 28<br>29 30 31</p></div>
      <div class="month"><b>5</b><p>1 2 3 4 5 6 7<br>8 9 10 11 12 13 14<br>15 16 17 18 19 20 21<br>22 23 24 25 26 27 28<br>29 30 31</p></div>
      <div class="month"><b>6</b><p>1 2 3 4 5 6 7<br>8 9 10 11 12 13 14<br>15 16 17 18 19 20 21<br>22 23 24 25 26 27 28<br>29 30 31</p></div>
      <div class="month"><b>7</b><p>1 2 3 4 5 6 7<br>8 9 10 11 12 13 14<br>15 16 17 18 19 20 21<br>22 23 24 25 26 27 28<br>29 30 31</p></div>
      <div class="month"><b>8</b><p>1 2 3 4 5 6 7<br>8 9 10 11 12 13 14<br>15 16 17 18 19 20 21<br>22 23 24 25 26 27 28<br>29 30 31</p></div>
      <div class="month"><b>9</b><p>1 2 3 4 5 6 7<br>8 9 10 11 12 13 14<br>15 16 17 18 19 20 21<br>22 23 24 25 26 27 28<br>29 30 31</p></div>
      <div class="month"><b>10</b><p>1 2 3 4 5 6 7<br>8 9 10 11 12 13 14<br>15 16 17 18 19 20 21<br>22 23 24 25 26 27 28<br>29 30 31</p></div>
      <div class="month"><b>11</b><p>1 2 3 4 5 6 7<br>8 9 10 11 12 13 14<br>15 16 17 18 19 20 21<br>22 23 24 25 26 27 28<br>29 30 31</p></div>
      <div class="month"><b>12</b><p>1 2 3 4 5 6 7<br>8 9 10 11 12 13 14<br>15 16 17 18 19 20 21<br>22 23 24 25 26 27 28<br>29 30 31</p></div>
    </div>
  </div>
</section>

<section class="panel back-bottom" aria-label="裏面台紙">
  <svg class="fold-notch" viewBox="0 0 274 150" aria-hidden="true">
    <line x1="0" y1="120" x2="110" y2="120" stroke="#b9b9b9" stroke-width="1"/>
    <polyline points="110,120 137,140 164,120" fill="none" stroke="#b9b9b9" stroke-width="1"/>
    <line x1="164" y1="120" x2="274" y2="120" stroke="#b9b9b9" stroke-width="1"/>
  </svg>
</section>

<div class="brand"><span class="dot"></span>LUNA</div>
<div class="footer-band">新規オープン美容院　ロゴマーク提案</div>

</body>
</html>
```